Business card design needed

I am a local business in the Blue Mountains area of Sydney. I am a sole trader and the business has been operating 7 months. To date the business has been built on referrals only and all my clinets for both home & commercial services are themselves business owners. I specialise in Home and Office cleaning and small business cleaning for example cafes, restuarants, health clinics.
I would like a clean looking design( maybe a white background). If its possible(not madatory) to incorporate a duster, or mop & bucket into the design or roof tops to communicate business premises that would be great. I would like my clients to know what the business is from the card. My uniform is navy with red/pink logo on .Attatched is the unifrom logo but it is not critical to match the font for the business card.
please put my name on contact details; Carol Whitby, Business owner.
Updates
Thank you very much to all the designers and their work efforts to submit a design for Bright Feather Domestic Services. I have made a decision to accept the deign that Velo Design of the United States submitted. Again Many thanks. Carol
Target Market(s)
business owners, generally women between 35-55
Industry/Entity Type
Small Business
Contact Information for Business Card
Bright Feather Domestic Services,
specialist in Home & Small business cleaning
Ferncliff NSW
tel: 0491570156 0491tidyup
Logo Text
Bright Feather Domestic Servies
Logo styles of interest
Emblem Logo
Abstract Logo
Wordmark Logo
Look and feel

```html
<!DOCTYPE html>
<html lang="en">
<head>
<meta charset="utf-8">
<title>Bright Feather Domestic Services – Business Card</title>
<link rel="stylesheet" href="https://fonts.googleapis.com/css2?family=Source+Sans+3:wght@400;600;700&display=swap">
<style>
  :root {
    --navy: #0f2550;
    --navy-deep: #0a1a3c;
    --stripe-navy: #27336b;
    --red: #c00812;
    --red-bright: #e41c2a;
    --sky: #b9d3e6;
    --silver: #b8bcc2;
    --paper: #fbfbfb;
    --stage-a: #5a3a3a;
    --stage-b: #2c2440;
    --ink-white: #ffffff;
  }
  * { box-sizing: border-box; margin: 0; padding: 0; }
  html, body { width: 1200px; height: 800px; overflow: hidden; }
  body {
    background: radial-gradient(ellipse at 55% 40%, var(--stage-a), var(--stage-b));
    font-family: "Source Sans 3", Arial, sans-serif;
    position: relative;
  }
  .card {
    position: absolute;
    top: 252px;
    width: 520px;
    height: 297px;
    background: var(--paper);
    overflow: hidden;
    box-shadow: 0 10px 30px rgba(0,0,0,.35);
  }
  .card-front { left: 50px; }
  .card-back { left: 630px; }
  .card-art { position: absolute; inset: 0; width: 100%; height: 100%; }

  .brand {
    position: absolute;
    left: 120px;
    top: 150px;
    color: var(--navy);
    font-weight: 600;
    line-height: 1.1;
  }
  .brand-name { font-size: 40px; display: block; }
  .brand-tagline { font-size: 19px; display: block; margin-top: 4px; padding-left: 30px; }

  .duster-art {
    position: absolute;
    right: 22px;
    bottom: 22px;
    width: 80px;
    height: 120px;
    background: linear-gradient(160deg, #ececec, #d8d8d8);
  }

  .owner {
    position: absolute;
    left: 40px;
    top: 16px;
    color: var(--ink-white);
  }
  .owner-name { font-size: 44px; font-weight: 700; line-height: 1; letter-spacing: -.5px; }
  .owner-role { font-size: 17px; margin-top: 2px; padding-left: 40px; }

  .contact-list {
    position: absolute;
    left: 28px;
    top: 108px;
    list-style: none;
    color: var(--ink-white);
    font-size: 14px;
    line-height: 1.2;
  }
  .contact-list li { display: flex; align-items: flex-start; gap: 10px; margin-bottom: 9px; }
  .contact-icon { width: 14px; height: 14px; flex: none; margin-top: 1px; }
  .contact-letter { width: 14px; flex: none; font-weight: 700; font-size: 12px; text-align: center; }
</style>
</head>
<body>

  <section class="card card-front" aria-label="Card front">
    <svg class="card-art" viewBox="0 0 520 297" aria-hidden="true">
      <path d="M0 70 Q260 -10 520 150 L520 165 Q260 10 0 78 Z" fill="var(--silver)"/>
      <path d="M0 62 Q270 -25 520 130 L520 152 Q260 -8 0 70 Z" fill="var(--navy)"/>
      <path d="M60 44 Q290 -20 520 140 L520 150 Q280 -5 60 48 Z" fill="var(--sky)"/>
      <path d="M150 25 Q330 -15 520 100 L520 132 Q300 -10 150 30 Z" fill="var(--red-bright)"/>
    </svg>
    <div class="duster-art" role="img" aria-label="Faint grey illustration of a feather duster"></div>
    <h1 class="brand">
      <span class="brand-name">Bright Feather</span>
      <span class="brand-tagline">Domestic Services</span>
    </h1>
  </section>

  <section class="card card-back" aria-label="Card back">
    <svg class="card-art" viewBox="0 0 520 297" aria-hidden="true">
      <rect width="520" height="297" fill="var(--red)"/>
      <rect width="520" height="92" fill="var(--navy)"/>
      <path d="M400 0 Q330 150 345 297 L520 297 L520 0 Z" fill="var(--paper)"/>
      <rect x="452" y="0" width="34" height="297" fill="var(--stripe-navy)"/>
      <line x1="448" y1="0" x2="448" y2="297" stroke="var(--silver)" stroke-width="1" stroke-dasharray="3 2"/>
    </svg>

    <div class="owner">
      <h2 class="owner-name">Carol Whitby</h2>
      <p class="owner-role">Business owner</p>
    </div>

    <ul class="contact-list">
      <li>
        <svg class="contact-icon" viewBox="0 0 14 14" aria-hidden="true"><path d="M3 1 L5 1 L6 4 L4.5 5.5 Q6 8.5 8.5 9.5 L10 8 L13 9 L13 11 Q12 13 10 13 Q2 11 1 3 Q1 1 3 1 Z" fill="currentColor"/></svg>
        <span>tel: 0491570156</span>
      </li>
      <li>
        <svg class="contact-icon" viewBox="0 0 14 14" aria-hidden="true"><circle cx="7" cy="7" r="6" fill="currentColor"/></svg>
        <span>specialist in Home &amp; Small business<br>cleaning</span>
      </li>
      <li>
        <svg class="contact-icon" viewBox="0 0 14 14" aria-hidden="true"><rect x="1" y="3" width="12" height="8" fill="currentColor"/><path d="M1 3 L7 8 L13 3" stroke="var(--red)" stroke-width="1.2" fill="none"/></svg>
        <span>brightfeather@mailhub.com.au</span>
      </li>
      <li>
        <span class="contact-letter">w</span>
        <span>www.brightfeather.com.au</span>
      </li>
      <li>
        <svg class="contact-icon" viewBox="0 0 14 14" aria-hidden="true"><path d="M7 13 Q2 7 2 5 A5 5 0 0 1 12 5 Q12 7 7 13 Z" fill="currentColor"/><circle cx="7" cy="5" r="1.8" fill="var(--red)"/></svg>
        <span>Ferncliff NSW</span>
      </li>
    </ul>
  </section>

</body>
</html>
```